Off Grid consulting and outdoor products needs a website

We need a website design to help launch our new business. Its a business that plans to offer Off-grid conslting and outdoor survival products to people who are looking to relocate or vacation to properties/homes that are Off-grid. We plan to offer design plans for homes/cabins, renewable energy systems for power/heating etc, survival products for outdoor vacations/living. We also do consulting and project management for those who want to design and build from scratch their dream off-grid home or vacation property. I've included our logo design for use.
Would like the website to include 5 pages.
www.ridgepinehaven.com
The main landing page (1)
want a video loop backround with a flyover of a cabin in the woods.
https://www.clipvaultora.com/video/clip-48291736-blue-sky-melting-snow-on-green-energy
(also need a backup static image of just high-shot of cabin in woods)
logo top left, Quoted string of text in the middle, over the video. and a CTA button to 'Contact us'
picture links below that to last 3 recent blog posts.
About Us page (2)
(example) https://larkwildgear.com/pages/about-lark
Blog page (3)
blog posts associated with pictures.
Consulting 'services' page (4)
-land services and moving off-grid
-Building off grid
-Renewable energy off-grid
-Sustainable farming and all season greenhouses
Store page 'comming soon' (5)
(Example) http://timberly.crestlayouts.com/demo-1/demo.html

Target Market(s)

Outdoor enthusiasts and people who want to escape their city life

Coding

Coded - Design and coding required

Requirements
Must have
• Outdoor feel, woods, cabin, reneable energy (solar, geothermal, greenhouses, water wells)

```html
<!DOCTYPE html>
<html lang="en">
<head>
<meta charset="utf-8">
<title>Ridgepine Haven — Off-Grid Consulting</title>
<link href="https://fonts.googleapis.com/css2?family=Oswald:wght@500;600;700&family=Poppins:wght@400;500&display=swap" rel="stylesheet">
<style>
:root{
  --forest:#3f4c3e;
  --forest-deep:#263024;
  --sage:#7a9770;
  --sage-light:#9db593;
  --ink:#1d1f1c;
  --muted:#555;
  --mist:#f3f5f2;
  --white:#fff;
}
*{box-sizing:border-box;margin:0;padding:0}
html,body{width:1200px;height:3897px;overflow:hidden}
body{position:relative;font-family:"Poppins",sans-serif;color:var(--ink);background:var(--white)}
.abs{position:absolute}
.heading{font-family:"Oswald",sans-serif;font-weight:600;text-transform:uppercase;letter-spacing:.2px}
.brand{font-family:"Oswald",sans-serif;font-weight:700;text-transform:uppercase;color:var(--ink);display:flex;align-items:center;gap:8px;line-height:1}
.brand .mark{width:14px;height:14px;background:currentColor;flex:none}
.brand.light{color:var(--white)}
.btn{position:absolute;display:flex;font-family:"Oswald",sans-serif;font-weight:500;text-transform:uppercase;font-size:16px;color:var(--white);text-decoration:none}
.btn .label{flex:1;display:flex;align-items:center;justify-content:center}
.btn .go{width:62px;display:flex;align-items:center;justify-content:center;clip-path:polygon(14px 0,100% 0,100% 100%,0 100%);margin-left:-14px}
.btn svg{width:20px;height:20px}
/* header */
.topline{font-size:15px;display:flex;align-items:center;gap:12px}
.topline b{font-weight:500}
.ring{width:38px;height:38px;border:1.5px solid #999;border-radius:50%;display:flex;align-items:center;justify-content:center}
.nav{font-family:"Oswald",sans-serif;font-size:16px;text-transform:uppercase}
.nav a{color:#333;text-decoration:none;position:absolute;top:0;white-space:nowrap}
.nav a.active{color:var(--sage)}
/* hero */
.hero-band{left:454px;top:300px;width:746px;height:441px;background:var(--sage);border-radius:0 0 140px 40px}
.hero{left:0;top:126px;width:1200px;height:597px;border-radius:0 0 140px 0;background:linear-gradient(100deg,#1f261d 0%,#2c3729 45%,#3a4636 75%,#2a3327 100%);overflow:hidden}
.hero .welcome{left:92px;top:160px;color:#fff;font-size:37px;display:flex;align-items:center;gap:12px}
.hero .welcome i{display:block;width:82px;height:3px;background:#fff}
.hero h1{left:90px;top:200px;color:#fff;font-size:70px;line-height:1}
.hero p{left:93px;top:288px;width:420px;color:#fff;font-size:19.5px;line-height:33px}
.hero .ghost{left:640px;top:300px;font-size:92px;color:rgba(255,255,255,.08);line-height:1}
.chev{top:220px;width:36px;height:60px}
/* section heads */
.sec-head{left:0;width:1200px;text-align:center}
.sec-head .brand{justify-content:center;font-size:22px}
.sec-head h2{font-size:37px;margin-top:10px;line-height:1.2}
.sec-head .rule{width:79px;height:4px;background:var(--forest);margin:8px auto 0}
.sec-head.light h2{color:#fff}
.sec-head.light .rule{background:#fff}
/* blog */
.dots{left:67px;top:964px;width:175px;height:216px;background-image:radial-gradient(var(--sage) 2px,transparent 2.5px);background-size:14px 14px}
.feature{left:92px;top:990px;width:507px;height:348px;border-radius:14px;overflow:hidden;background:linear-gradient(180deg,#5f7b47 0%,#4a5a35 40%,#2e3424 75%,#1a1d16 100%);box-shadow:0 20px 40px rgba(0,0,0,.18)}
.date{font-size:15px;color:var(--sage);display:flex;align-items:center;gap:6px}
.feature .date{position:absolute;left:32px;top:226px;color:#cfd8c8}
.feature h3{position:absolute;left:32px;top:254px;color:#fff;font-family:"Oswald",sans-serif;font-weight:500;font-size:22px;line-height:30px}
.thumb{left:626px;width:199px;height:161px;border-radius:12px}
.post-title{left:844px;font-family:"Oswald",sans-serif;font-weight:500;font-size:19px;line-height:28px;width:250px}
.view-all{left:528px;top:1387px;font-family:"Oswald",sans-serif;font-weight:500;font-size:16px;color:#333;text-transform:uppercase;display:flex;align-items:center;gap:8px}
.view-all span{border-bottom:1.5px solid #333}
/* services */
.services{left:0;top:1472px;width:1200px;height:684px;background:linear-gradient(180deg,#3d4a3b 0%,#4a5846 45%,#3a4637 100%)}
.card{top:1711px;width:241px;height:377px;background:#fff;border-radius:14px;text-align:center}
.card.active{background:var(--sage)}
.card svg.icon{position:absolute;left:85px;top:36px;width:70px;height:70px}
.card h4{position:absolute;left:0;top:128px;width:100%;font-family:"Oswald",sans-serif;font-weight:500;font-size:18px;line-height:28px;text-transform:uppercase}
.card p{position:absolute;left:18px;top:198px;width:205px;font-size:15px;line-height:28px;color:#444}
.card.active h4,.card.active p{color:#fff}
.card .btn{left:41px;top:301px;width:161px;height:43px;font-size:15px}
/* about */
.about{left:0;top:2156px;width:1200px;height:587px;background:var(--mist)}
.about-title{left:599px;top:2218px;font-size:40px;line-height:44px}
.about-copy{left:599px;top:2338px;width:505px}
.about-copy p{font-size:16.5px;line-height:30px;color:#444;margin-bottom:15px}
/* contact */
.contact-band{left:0;top:3100px;width:738px;height:347px;background:var(--sage);border-radius:0 0 40px 140px}
.contact{left:0;top:2743px;width:1200px;height:684px;background:linear-gradient(180deg,#1f261d 0%,#293226 50%,#232b21 100%);border-radius:0 0 0 140px}
.field{background:#fff;font-size:15px;color:#444;padding:0 18px;display:flex;align-items:center}
.field.area{align-items:flex-start;padding-top:14px}
/* footer */
.f-head{font-family:"Oswald",sans-serif;font-weight:600;font-size:19px;text-transform:uppercase}
.f-link{font-size:15px;color:#333}
.social{top:3685px;width:40px;height:40px;border-radius:50%;background:var(--forest)}
.f-contact{left:483px;display:flex;align-items:center;gap:14px;font-size:15.5px;line-height:25px;color:#333}
.f-contact .pin{width:40px;height:40px;border-radius:50%;background:var(--forest);display:flex;align-items:center;justify-content:center;flex:none}
.newsletter{left:831px;top:3669px;width:275px;height:52px;display:flex}
.newsletter .in{flex:1;background:#eceeea;display:flex;align-items:center;padding-left:18px;font-size:15px;color:#444}
.newsletter .send{width:57px;background:var(--sage);display:flex;align-items:center;justify-content:center}
.divider{left:92px;top:3828px;width:1014px;height:1px;background:#ccc}
.copy{left:0;top:3850px;width:1200px;text-align:center;font-size:15px;color:#333}
</style>
</head>
<body>

<!-- header -->
<div class="abs brand" style="left:92px;top:48px;font-size:26px"><span class="mark"></span>Ridgepine Haven</div>
<div class="abs topline" style="left:542px;top:8px">
  <span class="ring"><svg width="18" height="18" viewBox="0 0 24 24" fill="none" stroke="#555" stroke-width="2"><rect x="3" y="6" width="18" height="13" rx="2"/><path d="M3 7l9 6 9-6"/></svg></span>
  <span><b>Email :</b> contact@ridgepinehaven.com</span>
</div>
<div class="abs topline" style="left:890px;top:8px">
  <span class="ring"><svg width="18" height="18" viewBox="0 0 24 24" fill="none" stroke="#555" stroke-width="2"><path d="M5 3h4l2 5-3 2a11 11 0 0 0 6 6l2-3 5 2v4a2 2 0 0 1-2 2A17 17 0 0 1 3 5a2 2 0 0 1 2-2z"/></svg></span>
  <span><b>Phone :</b> 123-456-7890</span>
</div>
<nav class="abs nav" style="left:0;top:78px;width:960px">
  <a class="active" style="left:608px">• Home</a>
  <a style="left:690px">• About Us</a>
  <a style="left:792px">• Blog</a>
  <a style="left:861px">• Services</a>
</nav>
<a class="btn" style="left:967px;top:68px;width:139px;height:42px;font-size:17px">
  <span class="label" style="background:var(--forest)">Store</span>
  <span class="go" style="background:var(--ink);width:56px"><svg viewBox="0 0 24 24" fill="none" stroke="#fff" stroke-width="2"><path d="M4 12h16M14 6l6 6-6 6"/></svg></span>
</a>

<!-- hero -->
<div class="abs hero-band"></div>
<section class="abs hero" role="img" aria-label="Forest at dusk with a cabin among tall pines">
  <div class="abs heading welcome">Welcome to <i></i></div>
  <h1 class="abs heading">Ridgepine Haven</h1>
  <p class="abs">We offer Off-grid conslting and outdoor survival products to people</p>
  <div class="abs heading ghost">Ridgepine<br>Haven</div>
  <svg class="abs chev" style="left:20px" viewBox="0 0 36 60" fill="none" stroke="#fff" stroke-width="2.5"><path d="M30 4L6 30l24 26"/></svg>
  <svg class="abs chev" style="left:1146px" viewBox="0 0 36 60" fill="none" stroke="#fff" stroke-width="2.5"><path d="M6 4l24 26L6 56"/></svg>
</section>
<a class="btn" style="left:92px;top:504px;width:203px;height:51px">
  <span class="label" style="background:var(--sage)">Contact Us</span>
  <span class="go" style="background:#fff"><svg viewBox="0 0 24 24" fill="none" stroke="#333" stroke-width="2"><path d="M4 12h16M14 6l6 6-6 6"/></svg></span>
</a>

<!-- blog -->
<div class="abs sec-head" style="top:820px">
  <div class="brand" style="justify-content:center"><span class="mark"></span>Ridgepine Haven</div>
  <h2 class="heading">Recent Blog Posts</h2>
  <div class="rule"></div>
</div>
<div class="abs dots"></div>
<article class="abs feature" role="img" aria-label="Wooden cabin with a wraparound deck in the forest">
  <div class="date"><svg width="14" height="14" viewBox="0 0 24 24" fill="currentColor"><rect x="3" y="5" width="18" height="16" rx="2"/></svg>11 Mar 2022</div>
  <h3>Nemo enim ipsam voluptatem quia voluptas<br>sit aspernatur do amet</h3>
</article>

<div class="abs thumb" style="top:990px;background:linear-gradient(135deg,#7fa24a,#5e8233 55%,#3e4f8a)" role="img" aria-label="Solar panels on green grass"></div>
<div class="abs date" style="left:844px;top:992px"><svg width="14" height="14" viewBox="0 0 24 24" fill="currentColor"><rect x="3" y="5" width="18" height="16" rx="2"/></svg>10 Feb 2022</div>
<div class="abs post-title" style="top:1022px">Nemo enim ipsam voluptatem<br>sit aspernatur do amet</div>
<a class="btn" style="left:844px;top:1101px;width:171px;height:43px;font-size:15px">
  <span class="label" style="background:var(--forest)">Read More</span>
  <span class="go" style="background:var(--sage);width:52px"><svg viewBox="0 0 24 24" fill="none" stroke="#fff" stroke-width="2"><path d="M4 12h16M14 6l6 6-6 6"/></svg></span>
</a>

<div class="abs thumb" style="top:1177px;background:linear-gradient(180deg,#d9c4a5,#b99a6e 55%,#6f6a3d)" role="img" aria-label="Wind turbines on rolling fields"></div>
<div class="abs date" style="left:844px;top:1180px"><svg width="14" height="14" viewBox="0 0 24 24" fill="currentColor"><rect x="3" y="5" width="18" height="16" rx="2"/></svg>28 Feb 2022</div>
<div class="abs post-title" style="top:1210px">Nemo enim ipsam voluptatem<br>sit aspernatur do amet</div>
<a class="btn" style="left:844px;top:1289px;width:171px;height:43px;font-size:15px">
  <span class="label" style="background:var(--forest)">Read More</span>
  <span class="go" style="background:var(--sage);width:52px"><svg viewBox="0 0 24 24" fill="none" stroke="#fff" stroke-width="2"><path d="M4 12h16M14 6l6 6-6 6"/></svg></span>
</a>
<div class="abs view-all"><span>View All Blogs</span><svg width="22" height="16" viewBox="0 0 24 16" fill="none" stroke="#333" stroke-width="2"><path d="M2 8h19M15 2l6 6-6 6"/></svg></div>

<!-- services -->
<section class="abs services" role="img" aria-label="Misty green hills with wind turbines"></section>
<div class="abs sec-head light" style="top:1545px">
  <div class="brand light" style="justify-content:center"><span class="mark"></span>Ridgepine Haven</div>
  <h2 class="heading">Our Services</h2>
  <div class="rule"></div>
</div>

<div class="abs card" style="left:92px">
  <svg class="icon" viewBox="0 0 70 70" fill="none" stroke="#3f4c3e" stroke-width="1.6"><path d="M4 4v62h62"/><path d="M10 58c14-4 22-18 26-30s10-20 24-22"/><circle cx="20" cy="40" r="2"/><circle cx="30" cy="50" r="2"/><circle cx="44" cy="30" r="2"/><circle cx="52" cy="18" r="2"/><circle cx="56" cy="40" r="2"/></svg>
  <h4>Land Services &amp;<br>Moving Off-Grid</h4>
  <p>Sed ut perspiciatis undero omnis iste natus error sit voluptatem accusan..</p>
  <a class="btn"><span class="label" style="background:var(--forest)">View More</span><span class="go" style="background:var(--sage);width:52px"><svg viewBox="0 0 24 24" fill="none" stroke="#fff" stroke-width="2"><path d="M4 12h16M14 6l6 6-6 6"/></svg></span></a>
</div>
<div class="abs card active" style="left:350px">
  <svg class="icon" viewBox="0 0 70 70" fill="none" stroke="#fff" stroke-width="1.8"><path d="M6 30L35 6l29 24"/><path d="M12 25v40h46V25"/><rect x="29" y="22" width="12" height="12"/><path d="M35 22v12M29 28h12"/><path d="M20 65V48h10v17M40 50h14v15"/></svg>
  <h4>Building<br>Off-Grid</h4>
  <p>Sed ut perspiciatis undero omnis iste natus error sit voluptatem accusan..</p>
  <a class="btn"><span class="label" style="background:#000">View More</span><span class="go" style="background:#fff;width:52px"><svg viewBox="0 0 24 24" fill="none" stroke="#3f4c3e" stroke-width="2"><path d="M4 12h16M14 6l6 6-6 6"/></svg></span></a>
</div>
<div class="abs card" style="left:608px">
  <svg class="icon" viewBox="0 0 70 70" fill="none" stroke="#3f4c3e" stroke-width="1.6"><circle cx="35" cy="14" r="6"/><path d="M35 2v3M35 23v3M23 14h3M44 14h3M27 6l2 2M41 6l2 2"/><path d="M14 32h42l8 18H6z"/><path d="M28 32l-3 18M42 32l3 18M10 41h50"/><path d="M35 50v14M25 64h20"/></svg>
  <h4>Renewable Energy<br>Off-Grid</h4>
  <p>Sed ut perspiciatis undero omnis iste natus error sit voluptatem accusan..</p>
  <a class="btn"><span class="label" style="background:var(--forest)">View More</span><span class="go" style="background:var(--sage);width:52px"><svg viewBox="0 0 24 24" fill="none" stroke="#fff" stroke-width="2"><path d="M4 12h16M14 6l6 6-6 6"/></svg></span></a>
</div>
<div class="abs card" style="left:865px">
  <svg class="icon" viewBox="0 0 70 70" fill="none" stroke="#3f4c3e" stroke-width="1.6"><circle cx="56" cy="12" r="5"/><path d="M8 36L35 16l27 20"/><path d="M14 32v32h42V32"/><path d="M35 58V44M35 48c-6 0-9-4-9-8 5 0 9 3 9 8zM35 48c6 0 9-4 9-8-5 0-9 3-9 8z"/><path d="M10 6l6 10M20 4l2 10"/></svg>
  <h4>Sustainable Farming &amp;<br>All Season Greenhouses</h4>
  <p>Sed ut perspiciatis undero omnis iste natus error sit voluptatem accusan..</p>
  <a class="btn"><span class="label" style="background:var(--forest)">View More</span><span class="go" style="background:var(--sage);width:52px"><svg viewBox="0 0 24 24" fill="none" stroke="#fff" stroke-width="2"><path d="M4 12h16M14 6l6 6-6 6"/></svg></span></a>
</div>

<!-- about -->
<section class="abs about"></section>
<svg class="abs" style="left:94px;top:2235px" width="432" height="432" viewBox="0 0 432 432">
  <circle cx="216" cy="216" r="216" fill="#3f4c3e"/>
  <circle cx="216" cy="216" r="200" fill="#fff"/>
  <circle cx="216" cy="216" r="186" fill="none" stroke="#7a9770" stroke-width="2"/>
</svg>
<div class="abs brand" style="left:170px;top:2410px;font-size:40px;line-height:1.05"><span class="mark" style="width:22px;height:22px"></span>Ridgepine<br>Haven</div>
<h2 class="abs heading about-title">About<br>Ridgepine Haven</h2>
<div class="abs about-copy">
  <p>Lorem ipsum dolor sit amet consectetur adipisicing elit sed do eiusmod tempor incididunt ut labore et dolore magna aliqua. Ut enim ad minim veniam quis nostrud exercitation ullamco laboris nisi ut aliquip ex ea commodo consequat. Duis aute irure dolor in reprehenderit in voluptate.</p>
  <p>Sunt in culpa qui officia deserunt mollit anim id est laborum Sed ut perspiciatis unde omnis iste natus error sit volup tos accusantium doloremque laudantium, totam rem.</p>
</div>
<a class="btn" style="left:599px;top:2619px;width:203px;height:53px">
  <span class="label" style="background:var(--forest)">Learn More</span>
  <span class="go" style="background:var(--sage)"><svg viewBox="0 0 24 24" fill="none" stroke="#fff" stroke-width="2"><path d="M4 12h16M14 6l6 6-6 6"/></svg></span>
</a>

<!-- contact -->
<div class="abs contact-band"></div>
<section class="abs contact" role="img" aria-label="Dim greenhouse interior with arched frame"></section>
<div class="abs sec-head light" style="top:2818px">
  <div class="brand light" style="justify-content:center"><span class="mark"></span>Ridgepine Haven</div>
  <h2 class="heading">Contact Us</h2>
  <div class="rule"></div>
</div>
<div class="abs field" style="left:259px;top:2996px;width:334px;height:51px">Enter Your Name</div>
<div class="abs field" style="left:607px;top:2996px;width:334px;height:51px">Email Address</div>
<div class="abs field" style="left:259px;top:3062px;width:682px;height:52px">Phone No</div>
<div class="abs field area" style="left:259px;top:3129px;width:682px;height:156px">Type your message</div>
<a class="btn" style="left:498px;top:3303px;width:204px;height:51px">
  <span class="label" style="background:var(--forest)">Submit Now</span>
  <span class="go" style="background:var(--sage)"><svg viewBox="0 0 24 24" fill="none" stroke="#fff" stroke-width="2"><path d="M4 12h16M14 6l6 6-6 6"/></svg></span>
</a>

<!-- footer -->
<div class="abs brand" style="left:92px;top:3570px;font-size:28px;line-height:1.05"><span class="mark"></span>Ridgepine<br>Haven</div>
<div class="abs social" style="left:95px"></div>
<div class="abs social" style="left:141px"></div>
<div class="abs social" style="left:187px"></div>

<div class="abs f-head" style="left:307px;top:3530px">Quick Links</div>
<div class="abs f-link" style="left:307px;top:3572px">• Home</div>
<div class="abs f-link" style="left:307px;top:3605px">• About Us</div>
<div class="abs f-link" style="left:307px;top:3639px">• Blog</div>
<div class="abs f-link" style="left:307px;top:3672px">• Services</div>
<div class="abs f-link" style="left:307px;top:3705px">• Store</div>
<div class="abs f-link" style="left:307px;top:3738px">• Contact</div>

<div class="abs f-head" style="left:483px;top:3530px">Contact Us</div>
<div class="abs f-contact" style="top:3576px"><span class="pin"><svg width="18" height="18" viewBox="0 0 24 24" fill="#fff"><path d="M12 2a7 7 0 0 0-7 7c0 5 7 13 7 13s7-8 7-13a7 7 0 0 0-7-7zm0 9.5A2.5 2.5 0 1 1 12 6.5a2.5 2.5 0 0 1 0 5z"/></svg></span><span>Sed ut perspiciatis unde<br>iste natus error sit vol</span></div>
<div class="abs f-contact" style="top:3640px"><span class="pin"><svg width="18" height="18" viewBox="0 0 24 24" fill="#fff"><path d="M5 3h4l2 5-3 2a11 11 0 0 0 6 6l2-3 5 2v4a2 2 0 0 1-2 2A17 17 0 0 1 3 5a2 2 0 0 1 2-2z"/></svg></span><span>123-456-7890</span></div>
<div class="abs f-contact" style="top:3700px"><span class="pin"><svg width="18" height="18" viewBox="0 0 24 24" fill="none" stroke="#fff" stroke-width="2"><rect x="3" y="6" width="18" height="13" rx="1"/><path d="M3 7l9 6 9-6"/></svg></span><span>contact@ridgepinehaven.com</span></div>

<div class="abs f-head" style="left:830px;top:3530px">Newsletter</div>
<div class="abs f-link" style="left:830px;top:3572px;width:275px;line-height:25px">Sign up for our monthly newsletter and receive latest update on your inbox</div>
<div class="abs newsletter">
  <div class="in">Email Adress..</div>
  <div class="send"><svg width="18" height="18" viewBox="0 0 24 24" fill="#fff"><path d="M5 3l16 9-16 9z"/></svg></div>
</div>
<div class="abs divider"></div>
<div class="abs copy">Copyright © 2022 Ridgepine Haven. All rights reserved.</div>

</body>
</html>
```